2 Elite Law Firms on 1 double-sided monument Sign

The original story: 2 separate law firms already have their own perfect individual sign monuments, one for each firm. However, we must now combine them into 1 monument.

Target Market(s)

high-end clientele

Industry/Entity Type

Legal

Requirements
Must have
• Sleek, equal representation of both firms.

```html
<!DOCTYPE html>
<html lang="en">
<head>
<meta charset="utf-8">
<title>Shared Monument Sign – Hollis &amp; Associates / KMV Law Group</title>
<link href="https://fonts.googleapis.com/css2?family=Cinzel:wght@400;500&display=swap" rel="stylesheet">
<style>
  :root {
    --page: #ffffff;
    --ink: #ffffff;
    --brown: #55281a;
    --brown-deep: #531f12;
    --plum: #5a3446;
    --blue: #2e52a3;
    --blue-deep: #233e92;
    --base-grey: #959498;
  }
  html, body {
    margin: 0;
    padding: 0;
    width: 1200px;
    height: 1200px;
    overflow: hidden;
    background: var(--page);
  }
  .canvas {
    position: relative;
    width: 1200px;
    height: 1200px;
    font-family: "Cinzel", "Times New Roman", serif;
    color: var(--ink);
  }
  .suite-plate, .monument-face, .monument-base {
    position: absolute;
    box-sizing: border-box;
  }
  .suite-plate {
    left: 144px;
    width: 147px;
    height: 367px;
    display: flex;
    flex-direction: column;
    align-items: center;
    padding-top: 62px;
  }
  .suite-plate--hollis { top: 141px; background: var(--brown); }
  .suite-plate--kmv { top: 653px; background: var(--blue-deep); }
  .suite-plate__name {
    font-size: 44px;
    line-height: 1;
    letter-spacing: -1px;
  }
  .suite-plate--kmv .suite-plate__name {
    font-size: 30px;
    margin-top: 8px;
    text-align: center;
  }
  .suite-plate__sub {
    display: block;
    font-size: 7px;
    letter-spacing: 2px;
    margin-top: 2px;
  }
  .suite-plate__number {
    font-size: 48px;
    line-height: 1;
    margin-top: 46px;
  }
  .suite-plate--kmv .suite-plate__number { margin-top: 40px; }

  .monument-face {
    left: 358px;
    width: 715px;
    height: 367px;
    display: flex;
    flex-direction: column;
    align-items: center;
    justify-content: center;
  }
  .monument-face--hollis {
    top: 141px;
    background: linear-gradient(70deg, var(--brown-deep) 15%, var(--plum) 50%, #4a4680 75%, var(--blue) 92%);
  }
  .monument-face--kmv {
    top: 653px;
    background: linear-gradient(110deg, var(--blue) 18%, #4a4680 35%, var(--plum) 60%, var(--brown-deep) 100%);
  }
  .monument-base {
    left: 391px;
    width: 649px;
    height: 63px;
    background: var(--base-grey);
  }
  .monument-base--top { top: 508px; }
  .monument-base--bottom { top: 1020px; }

  .firm-name {
    text-align: center;
    line-height: 1;
    font-weight: 400;
  }
  .firm-name__primary {
    display: block;
    font-size: 78px;
    letter-spacing: 4px;
  }
  .firm-name__secondary {
    display: block;
    font-size: 64px;
    letter-spacing: 3px;
    margin-top: 4px;
  }
  .firm-name__tagline {
    display: block;
    font-size: 26px;
    letter-spacing: 4px;
    margin-top: 14px;
  }
  .firm-name--kmv .firm-name__primary {
    font-size: 120px;
    letter-spacing: 6px;
  }
  .firm-name--kmv .firm-name__tagline {
    font-size: 30px;
    letter-spacing: 12px;
    margin-top: 10px;
  }
</style>
</head>
<body>
<main class="canvas">
  <section class="sign-side sign-side--hollis">
    <div class="suite-plate suite-plate--hollis">
      <div class="suite-plate__name">H&amp;A</div>
      <div class="suite-plate__number">717</div>
    </div>
    <div class="monument-face monument-face--hollis">
      <h1 class="firm-name firm-name--hollis">
        <span class="firm-name__primary">HOLLIS</span>
        <span class="firm-name__secondary">&amp; ASSOCIATES</span>
        <span class="firm-name__tagline">ATTORNEYS AT LAW</span>
      </h1>
    </div>
    <div class="monument-base monument-base--top"></div>
  </section>

  <section class="sign-side sign-side--kmv">
    <div class="suite-plate suite-plate--kmv">
      <div class="suite-plate__name">KMV<span class="suite-plate__sub">LAW GROUP</span></div>
      <div class="suite-plate__number">715</div>
    </div>
    <div class="monument-face monument-face--kmv">
      <h2 class="firm-name firm-name--kmv">
        <span class="firm-name__primary">KMV</span>
        <span class="firm-name__tagline">LAW GROUP</span>
      </h2>
    </div>
    <div class="monument-base monument-base--bottom"></div>
  </section>
</main>
</body>
</html>
```